Property investment company needs a letterhead design!

We are a new residential and commercial property investment company. Name of the company is Morvessa Group, LLC. We have a new logo and now we need letterhead! We prefer to have a professional and upscale appearance. We don't have any fixed requirements, so be creative! Thank you for considering this project. We are so excited to see what happens!

Target Market(s)

Professional

Industry/Entity Type

Real Estate Development

```html
<!DOCTYPE html>
<html lang="en">
<head>
<meta charset="utf-8">
<title>Morvessa Group, LLC — Letterhead</title>
<link href="https://fonts.googleapis.com/css2?family=Lato:wght@400;700;900&family=Great+Vibes&display=swap" rel="stylesheet">
<style>
  :root {
    --backdrop: #e4e4e4;
    --paper: #f7f7f7;
    --navy: #0c2340;
    --sky: #1a9ad6;
    --ink: #4a4a4a;
    --ink-dark: #1c1c1c;
    --rule: #9a9a9a;
  }
  * { margin: 0; padding: 0; box-sizing: border-box; }
  html, body { width: 1200px; height: 900px; overflow: hidden; background: var(--backdrop); }
  body { position: relative; font-family: "Lato", sans-serif; color: var(--ink); }

  .sheet {
    position: absolute; top: 143px; width: 417px; height: 585px;
    background: linear-gradient(160deg, #ffffff 0%, var(--paper) 60%, #f1f1f1 100%);
    box-shadow: 0 2px 6px rgba(0,0,0,0.12);
    overflow: hidden;
  }
  .sheet--letter { left: 232px; }
  .sheet--blank { left: 670px; }

  .brand {
    position: absolute; left: 37px; top: 36px;
    display: flex; align-items: center; gap: 5px;
  }
  .brand__dot { width: 10px; height: 10px; border-radius: 50%; background: var(--sky); }
  .brand__name { font-weight: 900; font-size: 15px; letter-spacing: 0.3px; color: var(--navy); }

  .contact {
    position: absolute; top: 39px; left: 199px;
    display: flex; font-size: 6.6px; line-height: 8.4px; color: var(--ink);
  }
  .contact__list { list-style: none; padding-right: 7px; border-right: 0.6px solid var(--rule); }
  .contact__list li { display: flex; align-items: center; gap: 4px; }
  .contact__list svg { width: 5px; height: 5px; fill: var(--navy); }
  .contact__address { padding-left: 7px; font-style: normal; }

  .letter { position: absolute; left: 44px; top: 128px; width: 327px; font-size: 6.5px; line-height: 9.8px; }
  .letter__date { margin-bottom: 10px; }
  .letter__recipient { font-style: normal; margin-bottom: 19px; }
  .letter__recipient strong { color: var(--ink-dark); font-weight: 700; }
  .letter__salutation { margin-bottom: 10px; }
  .letter__body p { text-align: justify; margin-bottom: 9.8px; }
  .letter__closing { margin-top: 26px; }
  .letter__signature { font-family: "Great Vibes", cursive; font-size: 15px; color: var(--ink-dark); margin-top: 2px; margin-left: 4px; }

  .footer-wave { position: absolute; left: 0; bottom: 0; width: 417px; height: 55px; }
</style>
</head>
<body>

<article class="sheet sheet--letter">
  <header>
    <div class="brand"><span class="brand__dot"></span><span class="brand__name">MORVESSA</span></div>
    <div class="contact">
      <ul class="contact__list">
        <li><svg viewBox="0 0 10 10"><path d="M2 0l2 2-1 2c1 1 2 2 3 3l2-1 2 2-2 2C4 10 0 6 0 2z"/></svg>(555) 014-2273</li>
        <li><svg viewBox="0 0 10 10"><path d="M0 2h10v6H0z M0 2l5 4 5-4" /></svg>MorvessaLLC@mailbox.com</li>
        <li><svg viewBox="0 0 10 10"><circle cx="5" cy="5" r="5"/></svg>www.MorvessaLLC.com</li>
      </ul>
      <address class="contact__address">Morvessa Group, LLC<br>418 N. Alder Ave.<br>Fairhaven, MI 49010</address>
    </div>
  </header>

  <section class="letter">
    <p class="letter__date">01 January 2050</p>
    <address class="letter__recipient"><strong>Company (Pvt) Ltd.</strong><br>PO Box 3355 Mainville St<br>Sample City Country 3355</address>
    <p class="letter__salutation">Dear Daniel Ashford,</p>
    <div class="letter__body">
      <p>Lorem ipsum dolor sit amet, consectetuer adipiscing elit, sed diam nonummy nibh euismod tincidunt ut laoreet dolore magna aliquam erat volutpat. Ut wisi enim ad minim veniam, quis nostrud exerci tation ullamcorper suscipit lobortis nisl ut aliquip ex ea commodo consequat. Duis dolore te feugait nulla facilisi. Nam liber tempor cum soluta nobis eleifend option congue nihil imperdiet doming id quod mazim placerat facer possim assum. Lorem ipsum dolor sit amet, consectetuer adipiscing elit, sed diam nonummy nibh euismod tincidunt ut laoreet dolore magna aliquam erat volutpat. Ut wisi enim ad minim veniam, quis nostrud exerci tation ullamcorper suscipit lobortis nisl ut aliquip ex ea commodo consequat.</p>
      <p>Consectetuer adipiscing elit, sed diam nonummy nibh euismod tincidunt ut laoreet dolore magna aliquam erat volutpat. Ut wisi enim ad minim veniam, quis nostrud exerci tation ullamcorper suscipit lobortis nisl ut aliquip ex ea commodo consequat. Consectetuer adipiscing elit, sed diam nonummy nibh euismod tincidunt ut laoreet dolore magna aliquam erat volutpat. Ut wisi enim ad minim veniam, quis nostrud exerci tation ullamcorper suscipit lobortis nisl ut aliquip ex ea commodo consequat.</p>
      <p>Consectetuer adipiscing elit, sed diam nonummy nibh euismod tincidunt ut laoreet dolore magna aliquam erat volutpat. Ut wisi enim ad minim veniam, quis nostrud exerci tation ullamcorper suscipit lobortis nisl ut aliquip ex ea commodo consequat. Consectetuer adipiscing elit, sed diam nonummy nibh euismod tincidunt ut laoreet dolore magna aliquam erat volutpat. Ut wisi enim ad minim veniam, quis nostrud exerci tation ullamcorper suscipit lobortis nisl ut aliquip ex ea commodo consequat.</p>
    </div>
    <p class="letter__closing">Sincerely Yours</p>
    <p class="letter__signature">Thomas Reed Halvorsen</p>
  </section>

  <svg class="footer-wave" viewBox="0 0 417 55" preserveAspectRatio="none" aria-hidden="true">
    <path d="M0 10 Q190 62 417 4 L417 55 L0 55 Z" fill="var(--navy)"/>
    <path d="M0 5 Q170 52 320 40" fill="none" stroke="var(--sky)" stroke-width="2.4"/>
    <path d="M140 36 Q300 44 417 1" fill="none" stroke="var(--ink-dark)" stroke-width="1.2"/>
  </svg>
</article>

<article class="sheet sheet--blank">
  <header>
    <div class="brand"><span class="brand__dot"></span><span class="brand__name">MORVESSA</span></div>
    <div class="contact">
      <ul class="contact__list">
        <li><svg viewBox="0 0 10 10"><path d="M2 0l2 2-1 2c1 1 2 2 3 3l2-1 2 2-2 2C4 10 0 6 0 2z"/></svg>(555) 014-2273</li>
        <li><svg viewBox="0 0 10 10"><path d="M0 2h10v6H0z M0 2l5 4 5-4" /></svg>MorvessaLLC@mailbox.com</li>
        <li><svg viewBox="0 0 10 10"><circle cx="5" cy="5" r="5"/></svg>www.MorvessaLLC.com</li>
      </ul>
      <address class="contact__address">Morvessa Group, LLC<br>418 N. Alder Ave.<br>Fairhaven, MI 49010</address>
    </div>
  </header>

  <svg class="footer-wave" viewBox="0 0 417 55" preserveAspectRatio="none" aria-hidden="true">
    <path d="M0 10 Q190 62 417 4 L417 55 L0 55 Z" fill="var(--navy)"/>
    <path d="M0 5 Q170 52 320 40" fill="none" stroke="var(--sky)" stroke-width="2.4"/>
    <path d="M140 36 Q300 44 417 1" fill="none" stroke="var(--ink-dark)" stroke-width="1.2"/>
  </svg>
</article>

</body>
</html>
```